Law Firm Logo and Business Card Design

I need a logo and business card design for a law firm I just started. The law firm is named Law Office of Doreen K. Ashworth, LLC. The type of law I practice is Family Law, which includes divorce, custody, child support, alimony, property division, and the like. I would like to see designs that are unique and modern, yet sophisticated. I would also like to use the logo/design for my letterhead. I am not opposed to using some form of the scales of justice although I'd like something other than the typical, old fashioned scales of justice. I had considered a house made out of puzzle pieces with one puzzle piece pulled away from the others, with the logo text reading "Putting your life back together, one piece at a time." However, I don't want that particular design to look juvenile. I also would not be opposed to some form of my initials on the logo -- my initials are DKA. I am open to any other ideas you may have. I would like to see raised designs/lettering, and/or metallic finish. I like the colors black, white, gold, silver, and/or teal.

Industry/Entity Type

Law Firm

```html
<!DOCTYPE html>
<html lang="en">
<head>
<meta charset="utf-8">
<title>Law Office of Doreen K. Ashworth, LLC — Business Card</title>
<link rel="stylesheet" href="https://fonts.googleapis.com/css2?family=Noto+Sans:wght@400;700&display=swap">
<style>
  :root {
    --ink: #1a1a1a;
    --paper: #ffffff;
    --frame: #2a2a2a;
    --card-edge: #555555;
    --mark-tone: #c4c4c4;
  }
  * { margin: 0; padding: 0; box-sizing: border-box; }
  html, body { width: 1200px; height: 751px; overflow: hidden; background: var(--paper); }
  .canvas {
    position: relative;
    width: 1200px;
    height: 751px;
    border: 2px solid var(--frame);
    background: var(--paper);
    font-family: "Noto Sans", "Segoe UI", sans-serif;
    color: var(--ink);
  }
  .card {
    position: absolute;
    left: 61px; top: 64px;
    width: 1074px; height: 618px;
    border: 1px solid var(--card-edge);
  }
  .brand-mark {
    position: absolute;
    left: 796px; top: 52px;
    display: flex; align-items: center; gap: 16px;
  }
  .brand-mark__dot {
    width: 120px; height: 120px;
    border-radius: 50%;
    background: var(--mark-tone);
  }
  .brand-mark__name {
    font-size: 40px; font-weight: 700; letter-spacing: 2px;
  }
  .firm-name {
    position: absolute;
    left: 76px; top: 232px;
    font-size: 45px; font-weight: 700; line-height: 58px;
  }
  .divider {
    position: absolute;
    left: 74px; top: 354px;
    width: 838px; height: 2px;
    background: var(--ink);
  }
  .address {
    position: absolute;
    left: 76px; top: 384px;
    font-size: 28px; line-height: 38px;
    font-style: normal;
  }
  .contact-list {
    position: absolute;
    left: 487px; top: 382px;
    list-style: none;
  }
  .contact-list li {
    display: flex; align-items: center; gap: 14px;
    height: 49px;
    font-size: 28px;
  }
  .contact-list svg { width: 35px; height: 35px; flex: none; }
</style>
</head>
<body>
<div class="canvas">
  <section class="card">
    <div class="brand-mark">
      <span class="brand-mark__dot"></span>
      <span class="brand-mark__name">DKA</span>
    </div>

    <h1 class="firm-name">Law Office of<br>Doreen K. Ashworth, LLC.</h1>
    <div class="divider"></div>

    <address class="address">
      418 Chesapeake Landing Way<br>
      Suite 120<br>
      Severn Bay, MD 21409
    </address>

    <ul class="contact-list">
      <li>
        <svg viewBox="0 0 36 36" aria-hidden="true">
          <rect width="36" height="36" rx="7" fill="var(--ink)"/>
          <path d="M12 8c1.5-.8 2.6-.3 3.3 1l1.7 3.4c.5 1 .2 2-.7 2.6l-1.4 1c.8 2.3 2.2 4.3 4 5.8l1.4-.9c.9-.6 2-.4 2.6.5l2 3c.7 1.1.4 2.3-.8 3-3.5 2.1-8.3-.9-11.4-5.9S8.6 10 12 8z" fill="var(--paper)"/>
        </svg>
        <span>+443-555-0172</span>
      </li>
      <li>
        <svg viewBox="0 0 36 36" aria-hidden="true">
          <rect width="36" height="36" rx="7" fill="var(--ink)"/>
          <rect x="6" y="10" width="24" height="16" rx="1.5" fill="var(--paper)"/>
          <path d="M6.5 10.5 18 20l11.5-9.5M6.5 25.5l8.5-8M29.5 25.5l-8.5-8" fill="none" stroke="var(--ink)" stroke-width="1.6"/>
        </svg>
        <span>doreen@ashworthfamilylaw.com</span>
      </li>
      <li>
        <svg viewBox="0 0 36 36" aria-hidden="true">
          <rect width="36" height="36" rx="7" fill="var(--ink)"/>
          <g fill="none" stroke="var(--paper)" stroke-width="1.6">
            <circle cx="18" cy="18" r="11"/>
            <ellipse cx="18" cy="18" rx="5" ry="11"/>
            <path d="M7 18h22M9 12.5h18M9 23.5h18M18 7v22"/>
          </g>
        </svg>
        <span>www.ashworthfamilylaw.com</span>
      </li>
    </ul>
  </section>
</div>
</body>
</html>
```